Tessa Hollin's Contemporary HOMELINK Business Cards

I'd like a dark (almost black or black) background with some white lettering and some in a soft orange shade taken from the flowers. Print my photo large with all the lettering on the side opposite my photo. I'd like a simple, contemporary design similar to one I saw on your site. (All black with a tiny white line border inset from the edges. Glossy coating, please.

Target Market(s)

Real estate clients

Industry/Entity Type

Business

Contact Information for Business Card

medium weight cards

Font styles to use
Other font styles liked:
• Arial and perhaps Tessa in script above printed name

Requirements
Must have
• Tessa M. Hollin
• THP, KRA, BHS, SLR, e-DIR, HGA
• HOMELINK Circle of Honor, Gold Crest Realtor
• HOMELINK Career Distinction Prize
• HOMELINK Keystone - Boulder
• 303 555-0184 . 303 555-0127 cell
• Tessa@TessaHollinHomes.example
• ** Attached is the logo for the front of my business card. Please use the red one for HOMELINK KEYSTONE. Let me know if you need it in a different file type.
• On back of card please use this quote:
• “We have worked with Tessa Hollin on six real estate deals. Tessa is prompt, efficient, always does what she says she’s going to do, and she keeps the process moving without being pushy. She’s unbelievably organized and never misses a detail. After having dealt with many hundreds of professional people in our lives, Tessa stands out as one of the purely effective. Tessa is one of those wonderful people who is not only kind and empathetic, but strong. She’s a great listener. We trust her as an advisor. Tessa’s a smart lady who knows real estate—and this town—inside and out. Needless to say, we would work with Tessa Hollin again in an instant.
• ----- Mark Dunleavy
Nice to have
• several creative ideas
• probably should remove dark circle sculpture in background if it shows
• maybe Tessa in my script handwriting (orange)
Should not have
• don't know about this field

```html
<!DOCTYPE html>
<html lang="en">
<head>
<meta charset="utf-8">
<title>Tessa Hollin Business Cards</title>
<link rel="stylesheet" href="https://fonts.googleapis.com/css2?family=Dancing+Script:wght@500&family=Source+Sans+3:wght@400;700&display=swap">
<style>
  :root {
    --page-bg: #e4e4e6;
    --card-bg: #1f1f1f;
    --accent: #c0502a;
    --text-light: #ffffff;
    --photo-light: #c9b3a0;
    --photo-dark: #4a3d33;
  }
  html, body {
    margin: 0;
    padding: 0;
    width: 1200px;
    height: 1000px;
    overflow: hidden;
    background: var(--page-bg);
  }
  .sheet {
    position: relative;
    width: 1200px;
    height: 1000px;
  }
  .card {
    position: absolute;
    left: 265px;
    width: 666px;
    height: 398px;
    background: var(--card-bg);
    color: var(--text-light);
    font-family: "Source Sans 3", Arial, sans-serif;
  }
  .card--front { top: 73px; }
  .card--second { top: 532px; }
  .card__script {
    position: absolute;
    left: 34px;
    top: 33px;
    margin: 0;
    font-family: "Dancing Script", cursive;
    font-weight: 500;
    font-size: 96px;
    line-height: 1;
    color: var(--accent);
    white-space: nowrap;
  }
  .card__info {
    position: absolute;
    left: 33px;
    top: 179px;
    white-space: nowrap;
  }
  .card__name {
    margin: 0 0 6px;
    font-size: 20px;
    font-weight: 700;
    line-height: 24px;
  }
  .card__contact {
    list-style: none;
    margin: 0 0 6px;
    padding: 0;
  }
  .card__contact li {
    display: flex;
    align-items: center;
    gap: 4px;
    font-size: 16.5px;
    line-height: 22px;
  }
  .card__contact svg { width: 13px; height: 13px; flex: none; }
  .card__line {
    margin: 0;
    font-size: 16.5px;
    line-height: 22px;
  }
  .card__line--creds { margin-bottom: 4px; }
  .card__photo {
    position: absolute;
    left: 415px;
    top: 31px;
    width: 213px;
    height: 328px;
    border: 3px solid var(--accent);
    background: linear-gradient(160deg, var(--photo-light) 0%, #8f7866 45%, var(--photo-dark) 100%);
  }
</style>
</head>
<body>
<main class="sheet">
  <section class="card card--front">
    <p class="card__script">Tessa</p>
    <div class="card__info">
      <h1 class="card__name">Tessa M. Hollin</h1>
      <ul class="card__contact">
        <li><svg viewBox="0 0 14 14"><path d="M3 1 L5 4 L4 6 Q6 9 8 10 L10 9 L13 11 L11 13 Q5 12 1 3 Z" fill="var(--accent)"/></svg>303 555-0127</li>
        <li><svg viewBox="0 0 14 14"><path d="M3 1 L5 4 L4 6 Q6 9 8 10 L10 9 L13 11 L11 13 Q5 12 1 3 Z" fill="var(--accent)"/></svg>303 555-0184</li>
        <li><svg viewBox="0 0 14 14"><rect x="1" y="3" width="12" height="8" fill="var(--accent)"/><path d="M1 3 L7 8 L13 3" fill="none" stroke="var(--card-bg)" stroke-width="1"/></svg>Tessa@TessaHollinHomes.example</li>
      </ul>
      <p class="card__line card__line--creds">THP, KRA, BHS, SLR, e-DIR, HGA</p>
      <p class="card__line">HOMELINK Keystone - Boulder</p>
      <p class="card__line">HOMELINK Circle of Honor, Gold Crest Realtor</p>
      <p class="card__line">HOMELINK Career Distinction Prize</p>
    </div>
    <div class="card__photo" role="img" aria-label="Portrait photo of Tessa Hollin seated in a warm interior beside a vase of orange roses"></div>
  </section>

  <section class="card card--second">
    <p class="card__script">Tessa</p>
    <div class="card__info">
      <h2 class="card__name">Tessa M. Hollin</h2>
      <ul class="card__contact">
        <li><svg viewBox="0 0 14 14"><path d="M3 1 L5 4 L4 6 Q6 9 8 10 L10 9 L13 11 L11 13 Q5 12 1 3 Z" fill="var(--accent)"/></svg>303 555-0127</li>
        <li><svg viewBox="0 0 14 14"><path d="M3 1 L5 4 L4 6 Q6 9 8 10 L10 9 L13 11 L11 13 Q5 12 1 3 Z" fill="var(--accent)"/></svg>303 555-0184</li>
        <li><svg viewBox="0 0 14 14"><rect x="1" y="3" width="12" height="8" fill="var(--accent)"/><path d="M1 3 L7 8 L13 3" fill="none" stroke="var(--card-bg)" stroke-width="1"/></svg>Tessa@TessaHollinHomes.example</li>
      </ul>
      <p class="card__line card__line--creds">THP, KRA, BHS, SLR, e-DIR, HGA</p>
      <p class="card__line">HOMELINK Keystone - Boulder</p>
      <p class="card__line">HOMELINK Circle of Honor, Gold Crest Realtor</p>
      <p class="card__line">HOMELINK Career Distinction Prize</p>
    </div>
    <div class="card__photo" role="img" aria-label="Portrait photo of Tessa Hollin seated in a warm interior beside a vase of orange roses"></div>
  </section>
</main>
</body>
</html>
```